All stationery items: Business Cards, Letter Heads, and Envelops
Real Estate Business
All stationery items:  Business Cards, Letter Heads, and Envelops  - Real Estate
Creative Brief
Simple
Marcus Delvane
Real Estate Investor
82 Wrenfield Terrace Oakhurst NJ 07155
marcus@quillstonerealtyllc.example
quillstonerealtyllc.example
I have my blog website I would like to add on my car. its called go4renov.example. Also i like clean lines on the business card and other stationery items and keep the color scheme of the logo.
I would like my logo incorporate with a clear and simple design that makes the logo stand out even more.
marcusd418 marcusd418
Hi Everyone, I am liking the designs. I wanted to see if you could include other stationery such as the letter head. I would like to make my final decision seeing the total package. Thank you
I forgot to mention in my brief that I would like to see the different type of finishing option. For example, maybe a matte smooth finish. Something that is not like traditional cards. I'm looking for a premium finish.

```html
<!DOCTYPE html>
<html lang="en">
<head>
<meta charset="utf-8">
<title>Quillstone Realty Stationery</title>
<link rel="stylesheet" href="https://fonts.googleapis.com/css2?family=Montserrat:wght@400;600;700&display=swap">
<style>
  :root {
    --navy: #1f2d55;
    --green: #7cc143;
    --paper: #ffffff;
    --ink: #4a4f5c;
    --backdrop: #e4e5e7;
  }
  * { box-sizing: border-box; margin: 0; padding: 0; }
  html, body { width: 1200px; height: 799px; overflow: hidden; }
  body {
    background: var(--backdrop);
    font-family: "Montserrat", sans-serif;
    color: var(--ink);
    position: relative;
  }
  .sheet {
    position: absolute;
    background: var(--paper);
    box-shadow: 0 6px 18px rgba(0,0,0,.15);
    overflow: hidden;
  }
  .swoosh { position: absolute; right: 0; bottom: 0; }
  .brand {
    display: flex; align-items: center; gap: 6px;
    font-weight: 700; color: var(--navy); white-space: nowrap;
  }
  .brand-mark { background: var(--green); display: inline-block; }
  .details { font-size: 8px; line-height: 1.55; }
  .details .label { color: var(--green); font-weight: 600; }

  /* Letterhead */
  .letterhead { left: 60px; top: 60px; width: 440px; height: 622px; }
  .letterhead .brand { position: absolute; left: 36px; top: 40px; font-size: 17px; }
  .letterhead .brand-mark { width: 12px; height: 12px; }
  .letterhead .details { position: absolute; right: 36px; top: 36px; text-align: right; }
  .letterhead .swoosh { width: 230px; height: 260px; }

  /* Envelope */
  .envelope { left: 560px; top: 470px; width: 580px; height: 270px; }
  .envelope .brand { position: absolute; left: 32px; top: 32px; font-size: 16px; }
  .envelope .brand-mark { width: 11px; height: 11px; }
  .envelope .details { position: absolute; left: 32px; top: 60px; }
  .envelope .swoosh { width: 150px; height: 270px; }

  /* Business card back */
  .card-back { left: 560px; top: 60px; width: 280px; height: 160px; background: var(--navy); }
  .card-back .brand { position: absolute; left: 50%; top: 50%; transform: translate(-50%,-50%); color: var(--paper); font-size: 18px; }
  .card-back .brand-mark { width: 12px; height: 12px; }
  .card-back .swoosh { width: 120px; height: 90px; }

  /* Business card front */
  .card-front { left: 860px; top: 60px; width: 280px; height: 160px; }
  .card-front .name { position: absolute; left: 20px; top: 22px; font-size: 13px; font-weight: 700; color: var(--navy); }
  .card-front .role { position: absolute; left: 20px; top: 40px; font-size: 8px; color: var(--green); font-weight: 600; }
  .card-front .details { position: absolute; left: 20px; top: 66px; font-size: 7px; }
  .card-front .swoosh { width: 110px; height: 160px; }
</style>
</head>
<body>

<section class="sheet letterhead">
  <div class="brand"><span class="brand-mark"></span>Quillstone Realty</div>
  <div class="details">
    <div>82 Wrenfield Terrace Oakhurst NJ 07155</div>
    <div>marcus@quillstonerealtyllc.example</div>
    <div>quillstonerealtyllc.example</div>
  </div>
  <svg class="swoosh" viewBox="0 0 100 100" preserveAspectRatio="none" aria-hidden="true">
    <path d="M100 30 Q70 82 8 100 L22 100 Q78 84 100 44 Z" fill="var(--green)"/>
    <path d="M100 44 Q78 84 22 100 L100 100 Z" fill="var(--navy)"/>
  </svg>
</section>

<section class="sheet envelope">
  <div class="brand"><span class="brand-mark"></span>Quillstone Realty</div>
  <div class="details">
    <div>82 Wrenfield Terrace Oakhurst NJ 07155</div>
    <div>quillstonerealtyllc.example</div>
  </div>
  <svg class="swoosh" viewBox="0 0 100 100" preserveAspectRatio="none" aria-hidden="true">
    <path d="M100 10 Q55 60 40 100 L58 100 Q70 62 100 32 Z" fill="var(--green)"/>
    <path d="M100 32 Q70 62 58 100 L100 100 Z" fill="var(--navy)"/>
  </svg>
</section>

<section class="sheet card-back">
  <div class="brand"><span class="brand-mark"></span>Quillstone Realty</div>
  <svg class="swoosh" viewBox="0 0 100 100" preserveAspectRatio="none" aria-hidden="true">
    <path d="M100 20 Q60 80 0 100 L30 100 Q75 80 100 45 Z" fill="var(--green)"/>
    <path d="M100 45 Q75 80 30 100 L100 100 Z" fill="var(--paper)"/>
  </svg>
</section>

<section class="sheet card-front">
  <h1 class="name">Marcus Delvane</h1>
  <p class="role">Real Estate Investor</p>
  <div class="details">
    <div><span class="label">A</span> 82 Wrenfield Terrace Oakhurst NJ 07155</div>
    <div><span class="label">E</span> marcus@quillstonerealtyllc.example</div>
    <div><span class="label">W</span> quillstonerealtyllc.example</div>
    <div><span class="label">B</span> go4renov.example</div>
    <div><span class="label">S</span> marcusd418</div>
  </div>
  <svg class="swoosh" viewBox="0 0 100 100" preserveAspectRatio="none" aria-hidden="true">
    <path d="M100 0 Q75 55 55 100 L72 100 Q85 58 100 25 Z" fill="var(--green)"/>
    <path d="M100 25 Q85 58 72 100 L100 100 Z" fill="var(--navy)"/>
  </svg>
</section>

</body>
</html>
```